AUDITING SERVICES FOR IMPORT/EXPORT/LOGISTICS

* PROCUREMENT OF PARTS / SERVICES
* BOAT POSITIONING

Industry/Entity Type

Auditing

Contact Information for Business Card

TRV CONSULTANTS
(TIDEWIND HULLCRAFT PTY LTD) 17 KESTREL VISTA CORALWOOD SHORES
DAVID HARTLEY 0417286342 JULIE-KATE HARTLEY 0417286918 (ON OPPOSITE SIDE)

```html
<!DOCTYPE html>
<html lang="en">
<head>
<meta charset="utf-8">
<title>TRV Consultants – Business Card</title>
<link rel="stylesheet" href="https://fonts.googleapis.com/css2?family=Saira:wght@600;700&display=swap">
<style>
  :root {
    --backdrop: #e9e6e1;
    --card: #000000;
    --accent: #ffcc00;
    --ink-dark: #1f1f1f;
    --font-main: "Saira", "Arial Narrow", sans-serif;
  }
  * { margin: 0; padding: 0; box-sizing: border-box; }
  html, body {
    width: 1200px; height: 1000px; overflow: hidden;
    background: var(--backdrop);
    font-family: var(--font-main);
  }
  .canvas { position: relative; width: 1200px; height: 1000px; }
  .card {
    position: absolute; left: 227px; width: 746px; height: 460px;
    background: var(--card); color: var(--accent);
    box-shadow: 0 4px 14px rgba(0,0,0,0.25);
    overflow: hidden;
  }
  .card--front { top: 22px; }
  .card--back { top: 511px; }

  /* Front */
  .brand-mark {
    position: absolute; left: 102px; top: 119px;
    width: 134px; height: 134px; border-radius: 50%;
    background: var(--accent);
  }
  .brand-name {
    position: absolute; left: 257px; top: 152px;
    font-size: 52px; font-weight: 700; line-height: 1; letter-spacing: 0.5px;
    white-space: nowrap;
  }
  .front-entity {
    position: absolute; left: 0; right: 0; top: 296px; text-align: center;
    font-size: 24px; font-weight: 600; letter-spacing: 0.3px;
  }

  /* Back */
  .name-tab {
    position: absolute; left: 0; top: 49px; width: 435px; height: 98px;
    background: var(--accent); color: var(--ink-dark);
    border-radius: 0 32px 32px 0;
    padding: 18px 0 0 37px;
  }
  .tab-title { font-size: 30px; font-weight: 700; line-height: 1.1; letter-spacing: 0.3px; }
  .tab-entity { font-size: 14.5px; font-weight: 600; margin-top: 9px; }
  .address {
    position: absolute; left: 40px; top: 160px;
    display: flex; align-items: center; gap: 10px;
    font-size: 15px; font-weight: 600;
  }
  .address svg { width: 16px; height: 22px; fill: var(--accent); }
  .contact {
    position: absolute; left: 0; right: 0; text-align: center;
  }
  .contact--first { top: 240px; }
  .contact--second { top: 337px; }
  .contact-name { font-size: 30px; font-weight: 700; line-height: 1.2; letter-spacing: 0.3px; }
  .contact-phone {
    display: inline-flex; align-items: center; gap: 12px;
    font-size: 15px; font-weight: 600; margin-top: 6px;
  }
  .contact-phone svg { width: 20px; height: 20px; fill: var(--accent); }
</style>
</head>
<body>
<main class="canvas">
  <section class="card card--front" aria-label="Business card front">
    <div class="brand-mark"></div>
    <div class="brand-name">TRV CONSULTANTS</div>
    <div class="front-entity">TIDEWIND HULLCRAFT PTY LTD</div>
  </section>

  <section class="card card--back" aria-label="Business card back">
    <div class="name-tab">
      <div class="tab-title">TRV CONSULTANTS</div>
      <div class="tab-entity">TIDEWIND HULLCRAFT PTY LTD</div>
    </div>
    <div class="address">
      <svg viewBox="0 0 16 22" aria-hidden="true"><path d="M8 0C3.6 0 0 3.5 0 7.9 0 13.5 8 22 8 22s8-8.5 8-14.1C16 3.5 12.4 0 8 0zm0 11a3.2 3.2 0 1 1 0-6.4A3.2 3.2 0 0 1 8 11z"/></svg>
      <span>17 KESTREL VISTA CORALWOOD SHORES</span>
    </div>
    <div class="contact contact--first">
      <div class="contact-name">DAVID HARTLEY</div>
      <div class="contact-phone">
        <svg viewBox="0 0 24 24" aria-hidden="true"><path d="M6.6 10.8a15.1 15.1 0 0 0 6.6 6.6l2.2-2.2c.3-.3.7-.4 1-.2 1.1.4 2.3.6 3.6.6.6 0 1 .4 1 1V20c0 .6-.4 1-1 1C10.6 21 3 13.4 3 4c0-.6.4-1 1-1h3.5c.6 0 1 .4 1 1 0 1.3.2 2.5.6 3.6.1.3 0 .7-.2 1l-2.3 2.2z"/></svg>
        <span>0417286342</span>
      </div>
    </div>
    <div class="contact contact--second">
      <div class="contact-name">JULIE-KATE HARTLEY</div>
      <div class="contact-phone">
        <svg viewBox="0 0 24 24" aria-hidden="true"><path d="M6.6 10.8a15.1 15.1 0 0 0 6.6 6.6l2.2-2.2c.3-.3.7-.4 1-.2 1.1.4 2.3.6 3.6.6.6 0 1 .4 1 1V20c0 .6-.4 1-1 1C10.6 21 3 13.4 3 4c0-.6.4-1 1-1h3.5c.6 0 1 .4 1 1 0 1.3.2 2.5.6 3.6.1.3 0 .7-.2 1l-2.3 2.2z"/></svg>
        <span>0417286918</span>
      </div>
    </div>
  </section>
</main>
</body>
</html>
```